Print Ad for Pilates Studio

I need a full color 1/4 page ad (size 5" tall x 3 3/4" wide) that includes our logo at top with this text:
Intro Specials for New Students:
3 Private Sessions for only $150 (normally $75/session)
3 Group Reformer Classes for $49 (normally $35/class)
5 Bootcamp Classes for only $29 (normally $15/class0
and might include the tree graphic, and the three small logos (QRN, Green-certified and Top Pick) at bottom plus our phone number really big
555-214-3096 and e-mail MarissaTolvane@mailbrook.example and website www.steadycorefit.example
Should look enticing and CLEAN

Target Market(s)

Older affluent market

Industry/Entity Type

Group

Requirements
Must have
• Clean lines
• Bold
• Classy
• some space
• Makes you want to take action now
Nice to have
• photo of people doing pilates
• Bold color like yellow, green, burgundy

```html
<!DOCTYPE html>
<html lang="en">
<head>
<meta charset="utf-8">
<title>Steady Core – Intro Specials</title>
<link href="https://fonts.googleapis.com/css2?family=Roboto:wght@300;400;500;700&family=Roboto+Condensed:wght@400;700&display=swap" rel="stylesheet">
<style>
  :root {
    --green-dark: #4b6a32;
    --green-mid: #6a9a3e;
    --green-text: #5e8a35;
    --gold: #c9962b;
    --ink: #3b3b3b;
    --ink-soft: #6b6b6b;
    --leaf: #e6f0da;
    --paper: #ffffff;
    --badge-slate: #6f87a8;
    --badge-green: #3d8a63;
    --badge-blue: #2f6fb2;
  }
  * { margin: 0; padding: 0; box-sizing: border-box; }
  html, body { width: 959px; height: 1200px; overflow: hidden; background: var(--paper); }
  body { font-family: "Roboto", Arial, sans-serif; color: var(--ink); }
  .ad { position: relative; width: 959px; height: 1200px; background: var(--paper); }

  .tree-art {
    position: absolute; left: 440px; top: 205px; width: 519px; height: 832px;
    background: radial-gradient(ellipse at 55% 35%, var(--leaf) 0%, rgba(230,240,218,0.6) 45%, rgba(255,255,255,0) 75%);
  }

  .brand { position: absolute; left: 0; top: 0; width: 959px; height: 210px; }
  .brand-name {
    position: absolute; right: 80px; top: 68px;
    font-family: "Roboto", Arial, sans-serif; font-weight: 500; font-size: 84px;
    color: var(--green-dark); letter-spacing: -1px; line-height: 1;
  }
  .brand-tagline {
    position: absolute; left: 354px; top: 164px; width: 525px; height: 36px;
    background: var(--green-dark); border-radius: 4px;
    color: #fff; font-weight: 500; font-size: 27px;
    display: flex; align-items: center; justify-content: center;
  }
  .brand-tagline sup { font-size: 14px; position: relative; top: -2px; }

  .offer-heading {
    position: absolute; left: 68px; top: 312px; width: 683px; height: 52px;
    background: var(--green-mid); border-radius: 12px;
    color: #fff; font-weight: 400; font-size: 43px; line-height: 52px; text-align: center;
  }

  .offers { position: absolute; left: 98px; top: 426px; width: 792px; list-style: none; }
  .offer { position: relative; height: 107px; padding-left: 46px; }
  .offer-bullet { position: absolute; left: 0; top: 9px; width: 30px; height: 30px; }
  .offer-title { font-size: 42px; font-weight: 400; line-height: 48px; }
  .offer-note { font-family: "Roboto Condensed", Arial, sans-serif; font-size: 21px; color: var(--ink-soft); }
  .offer-price {
    position: absolute; right: 0; top: -4px; font-weight: 700; font-size: 46px; color: var(--gold);
  }
  .offer:nth-child(2) .offer-price, .offer:nth-child(3) .offer-price { right: 22px; }

  .badges { position: absolute; top: 812px; left: 0; width: 959px; height: 130px; }
  .badge { position: absolute; }
  .badge-cert { left: 236px; top: 0; width: 136px; height: 128px; background: var(--badge-slate); border-radius: 6px; }
  .badge-green { left: 434px; top: 2px; width: 126px; height: 126px; background: var(--badge-green); border-radius: 50%; }
  .badge-award { left: 635px; top: 0; width: 116px; height: 128px; background: var(--badge-blue); border-radius: 6px; }

  .contact-line {
    position: absolute; top: 1012px; left: 0; width: 959px; text-align: center;
    font-family: "Roboto Condensed", Arial, sans-serif; font-weight: 700; font-size: 25px; color: var(--green-text);
  }
  .contact-line .sep { margin: 0 10px; }

  .phone-bar {
    position: absolute; left: 170px; top: 1076px; width: 620px; height: 124px;
    background: var(--green-dark); border-radius: 14px 14px 0 0;
    display: flex; align-items: center; justify-content: center; gap: 26px;
  }
  .phone-icon { width: 66px; height: 58px; }
  .phone-number { color: #fff; font-weight: 700; font-size: 66px; letter-spacing: 1px; }
</style>
</head>
<body>
<main class="ad">
  <div class="tree-art" role="img" aria-label="Soft pale green tree illustration with leafy branches"></div>

  <header class="brand">
    <div class="brand-name">steady core</div>
    <div class="brand-tagline"><span>Pilates &amp; Spiralform<sup>®</sup> Studio</span></div>
  </header>

  <h1 class="offer-heading">Intro Specials for New Students:</h1>

  <ul class="offers">
    <li class="offer">
      <svg class="offer-bullet" viewBox="0 0 30 30"><circle cx="15" cy="15" r="15" fill="var(--green-dark)"/><path d="M12 8l7 7-7 7" stroke="#fff" stroke-width="4" fill="none" stroke-linecap="round" stroke-linejoin="round"/></svg>
      <div class="offer-title">3 Private Sessions for only</div>
      <div class="offer-note">(normally $75/session)</div>
      <div class="offer-price">$150</div>
    </li>
    <li class="offer">
      <svg class="offer-bullet" viewBox="0 0 30 30"><circle cx="15" cy="15" r="15" fill="var(--green-dark)"/><path d="M12 8l7 7-7 7" stroke="#fff" stroke-width="4" fill="none" stroke-linecap="round" stroke-linejoin="round"/></svg>
      <div class="offer-title">3 Group Reformer Classes for</div>
      <div class="offer-note">(normally $35/class)</div>
      <div class="offer-price">$49</div>
    </li>
    <li class="offer">
      <svg class="offer-bullet" viewBox="0 0 30 30"><circle cx="15" cy="15" r="15" fill="var(--green-dark)"/><path d="M12 8l7 7-7 7" stroke="#fff" stroke-width="4" fill="none" stroke-linecap="round" stroke-linejoin="round"/></svg>
      <div class="offer-title">5 Bootcamp Classes for only</div>
      <div class="offer-note">(normally $15/class)</div>
      <div class="offer-price">$29</div>
    </li>
  </ul>

  <section class="badges">
    <div class="badge badge-cert" role="img" aria-label="QRN certification badge"></div>
    <div class="badge badge-green" role="img" aria-label="Green business program badge"></div>
    <div class="badge badge-award" role="img" aria-label="Top Pick award badge"></div>
  </section>

  <p class="contact-line">e: MarissaTolvane@mailbrook.example<span class="sep">|</span>w: www.steadycorefit.example</p>

  <footer class="phone-bar">
    <svg class="phone-icon" viewBox="0 0 66 58" aria-hidden="true">
      <path d="M4 20c0-9 13-15 29-15s29 6 29 15v4H48v-6c-4-2-9-3-15-3s-11 1-15 3v6H4z" fill="#fff"/>
      <path d="M14 28h38l6 26H8z" fill="#fff"/>
      <circle cx="33" cy="40" r="7" fill="var(--green-dark)"/>
    </svg>
    <span class="phone-number">555-214-3096</span>
  </footer>
</main>
</body>
</html>
```